Financial Services Company Needs New UI/UX

Hello!

We would like to see some UI/UX ideas for our software platform. I've attached a screen capture of our current "dashboard" (or main home page, essentially). We're looking for a very simple, clean, sleek design as there are many different pages throughout the system that will all need to coordinate. You can also view our website to see the colors and general "look" we have on there. It would be ideal for the portal to coordinate with the website since that is how they access the login page. Please submit your best ideas for the dashboard and we will reach out to our favorite designer to move forward with the rest of the pages. You can find our color hex codes on our website on the "Media" page. Should you need any other supporting logos or files please send us a message and we will try to accommodate.

Thanks!

Website: www.lendmarkbuilt.example

Target Market(s)

Our clients are contractors in the construction industry and our software helps them manage material purchases for their jobs.

Industry/Entity Type

Financial Service

Font styles to use
Sans Serif

Requirements
Must have
• The same content and language as the current dashboard but an updated look.
Should not have
• Too much distraction or busy patterns, we're looking for clean and simple and user friendly. Likely a solid or subtly textured background would be best.

```html
<!DOCTYPE html>
<html lang="en">
<head>
<meta charset="utf-8">
<title>Kestrelbeam Dashboard</title>
<link href="https://fonts.googleapis.com/css2?family=Roboto:wght@400;500;700&display=swap" rel="stylesheet">
<style>
:root{
  --sidebar:#2b2f34;
  --sidebar-active:#1d2023;
  --topbar:#2b2f34;
  --accent-blue:#4a8fd8;
  --amount-blue:#3f7fcb;
  --orange:#e8541e;
  --green:#3bb54a;
  --brown:#a8784a;
  --ink:#222;
  --nav-text:#c9ced4;
  --top-text:#8d939a;
  --page:#eef1f4;
  --panel-head:#cfdbe4;
  --line:#e3e7eb;
  --btn:#1f2226;
  --col-head:#b8864e;
}
*{box-sizing:border-box;margin:0;padding:0}
html,body{width:1200px;height:675px;overflow:hidden;background:#fff;font-family:"Roboto",Arial,sans-serif;color:var(--ink)}
.app{position:relative;width:1200px;height:675px}
.sidebar{position:absolute;left:0;top:0;width:219px;height:675px;background:var(--sidebar)}
.brand{height:75px;display:flex;align-items:center;padding-left:29px;gap:8px;color:#fff;font-size:14px;font-weight:400}
.brand-dot{width:30px;height:30px;border-radius:50%;background:var(--accent-blue)}
.nav{list-style:none}
.nav-item{position:absolute;left:0;width:219px;display:flex;align-items:center;gap:14px;padding-left:33px;color:var(--nav-text);font-size:12.8px;font-weight:400;line-height:1.2;text-transform:uppercase}
.nav-item svg{width:20px;height:20px;flex:none;stroke:var(--nav-text);fill:none;stroke-width:1.3}
.nav-item.active{top:75px;height:63px;background:var(--sidebar-active);color:var(--accent-blue);border-left:6px solid var(--accent-blue);padding-left:27px}
.nav-item.active svg{stroke:var(--accent-blue)}
.nav-item.active::after{content:"";position:absolute;right:0;top:24px;border:8px solid transparent;border-right-color:#fff}
.topbar{position:absolute;left:219px;top:0;width:981px;height:75px;background:var(--topbar);display:flex;align-items:center;color:var(--top-text);font-size:12px}
.contact{display:flex;align-items:center;gap:8px}
.contact svg{width:16px;height:16px;stroke:var(--top-text);fill:none;stroke-width:1.2}
.contact.phone{margin-left:39px}
.divider-v{width:1px;height:26px;background:#555a60;margin:0 29px 0 33px}
.user{margin-left:auto;margin-right:39px;display:flex;align-items:center;gap:8px;font-size:13.6px;color:#b9bec4}
.caret{width:0;height:0;border:6px solid transparent;border-top:7px solid var(--orange);margin:8px 16px 0 0}
.avatar{width:25px;height:25px;border-radius:50%;background:#6c727a}
.page-head{position:absolute;left:219px;top:75px;width:981px;height:63px;background:#fff}
.page-title{position:absolute;right:88px;top:18px;font-size:22px;font-weight:400;color:#222}
.menu-btn{position:absolute;right:39px;top:19px;width:25px;height:25px;background:var(--orange);display:flex;align-items:center;justify-content:center}
.menu-btn::before{content:"";border:5px solid transparent;border-top:6px solid #fff;margin-top:6px}
.summary{position:absolute;left:219px;top:138px;width:981px;height:256px;background:var(--page)}
.card{position:absolute;top:20px;width:288px;height:204px;background:#fff;text-align:center}
.card .badge{position:absolute;left:134px;top:-10px;width:20px;height:20px;border-radius:50%;background:var(--btn);color:#fff;font-size:11px;font-weight:700;line-height:20px}
.card .badge.action{background:var(--green)}
.card-title{height:47px;padding-top:28px;font-size:13.6px;font-weight:500;border-bottom:1px solid var(--line)}
.amount{margin-top:18px;font-size:29px;font-weight:700;color:var(--amount-blue)}
.detail{margin-top:19px;font-size:10px;color:#333;line-height:15.5px}
.detail.stacked{margin-top:7px}
.actions{position:absolute;left:0;right:0;top:161px;display:flex;justify-content:center;gap:4px}
.btn{height:25px;background:var(--btn);color:#fff;font-size:11px;border-radius:2px;display:flex;align-items:center;justify-content:center;padding:0 10px}
.legend{position:absolute;right:39px;top:234px;display:flex;gap:27px;font-size:10px;color:#555}
.legend span{display:flex;align-items:center;gap:5px}
.dot{width:12px;height:12px;border-radius:50%;color:#fff;font-size:8px;font-weight:700;display:inline-flex;align-items:center;justify-content:center;font-style:normal}
.dot.action{background:var(--green)}
.dot.info{background:var(--brown)}
.panel{position:absolute;top:407px;width:443px;height:250px;border:1px solid var(--line);background:#fff}
.panel.tasks{left:258px}
.panel.jobs{left:718px}
.panel-head{height:36px;background:var(--panel-head);display:flex;align-items:center;gap:9px;padding-left:12px;font-size:14.5px;font-weight:700}
.panel-head svg{width:19px;height:19px;stroke:#222;fill:none;stroke-width:1.5}
table{width:100%;border-collapse:collapse;table-layout:fixed;font-size:10px;color:#333}
th{height:35px;text-align:left;font-weight:400;font-size:11.5px;color:var(--col-head);padding-left:11px;white-space:nowrap}
td{height:35.6px;padding-left:11px;border-top:1px solid var(--line);line-height:12.5px}
th+th,td+td{border-left:1px solid var(--line)}
.jobs td.num{text-align:right;padding-right:12px}
.task-flag{width:20px;height:20px;border-radius:50%;background:var(--brown);color:#fff;font-weight:700;font-size:12px;display:flex;align-items:center;justify-content:center;margin-left:-2px}
</style>
</head>
<body>
<div class="app">
  <aside class="sidebar">
    <div class="brand"><span class="brand-dot"></span><span>Kestrelbeam</span></div>
    <ul class="nav">
      <li class="nav-item active"><svg viewBox="0 0 20 20"><circle cx="10" cy="10" r="8"/><path d="M10 10l4-4M5 12h2M13 12h2"/></svg>Dashboard</li>
      <li class="nav-item" style="top:152px;height:36px"><svg viewBox="0 0 20 20"><path d="M3 17l8-8M12 4l4 4-3 1-2-2zM4 3l4 4M3 6l3-3M12 12l5 5"/></svg>Job Center</li>
      <li class="nav-item" style="top:212px;height:36px"><svg viewBox="0 0 20 20"><rect x="2" y="4" width="16" height="12" rx="1"/><path d="M2 8h16M5 12h5"/></svg>Payments</li>
      <li class="nav-item" style="top:274px;height:36px"><svg viewBox="0 0 20 20"><path d="M2 7l8-4 8 4zM4 8v7M8 8v7M12 8v7M16 8v7M2 17h16"/></svg>Credit<br>Management</li>
      <li class="nav-item" style="top:337px;height:36px"><svg viewBox="0 0 20 20"><path d="M5 2h7l3 3v13H5zM7 8h6M7 11h6M7 14h6"/></svg>Prelien Center</li>
    </ul>
  </aside>

  <header class="topbar">
    <div class="contact phone"><svg viewBox="0 0 16 16"><circle cx="8" cy="8" r="7"/><path d="M5.5 4.5l1.5 1.5-1 1a5 5 0 003 3l1-1 1.5 1.5-1 1.5c-3 0-6-3-6-6z"/></svg>Support: 800-555-0142</div>
    <div class="divider-v"></div>
    <div class="contact"><svg viewBox="0 0 16 16"><rect x="1" y="3" width="14" height="10"/><path d="M1 3l7 6 7-6"/></svg>help@ridgelinesupply.example</div>
    <div class="user"><span class="caret"></span><span class="avatar"></span>ac101@demo.example</div>
  </header>

  <div class="page-head">
    <h1 class="page-title">Dashboard</h1>
    <div class="menu-btn"></div>
  </div>

  <section class="summary">
    <div class="card" style="left:39px">
      <span class="badge">i</span>
      <div class="card-title">AVAILABLE MASTER CREDIT</div>
      <div class="amount">$129,500.00</div>
      <div class="detail">Master Credit Limit: $250,000.00</div>
      <div class="actions"><div class="btn" style="width:132px">Setup New Job</div></div>
    </div>
    <div class="card" style="left:347px">
      <span class="badge">i</span>
      <div class="card-title">LAST PAYMENT</div>
      <div class="amount">$500.00</div>
      <div class="detail">Last Payment Date: 6/28/2016</div>
      <div class="actions"><div class="btn" style="width:120px">Veiw Payments</div><div class="btn" style="width:120px">Veiw Billings</div></div>
    </div>
    <div class="card" style="left:655px">
      <span class="badge action">!</span>
      <div class="card-title">NEXT PAYMENT</div>
      <div class="amount">$158.95</div>
      <div class="detail stacked">Due Date: 7/11/2016<br>Current Principal: $9,968.46<br>Minimum Interest/Fees: $158.95</div>
      <div class="actions"><div class="btn" style="width:132px">Make Payment</div></div>
    </div>
    <div class="legend">
      <span><i class="dot action">!</i>Indicates an action is required</span>
      <span><i class="dot info">?</i>Information only - no action required</span>
    </div>
  </section>

  <section class="panel tasks">
    <div class="panel-head"><svg viewBox="0 0 20 20"><rect x="3" y="3" width="14" height="15" rx="1"/><path d="M7 2h6v3H7zM6 9h8M6 12h8M6 15h5"/></svg>Task Summary</div>
    <table>
      <colgroup><col style="width:37px"><col style="width:150px"><col style="width:151px"><col></colgroup>
      <thead><tr><th></th><th>Task</th><th>Status</th><th>Received</th></tr></thead>
      <tbody>
        <tr><td><span class="task-flag">?</span></td><td>Supplier Invoice</td><td>Confirmation by Account Manager Pending</td><td>5/01/2016</td></tr>
        <tr><td></td><td></td><td></td><td></td></tr>
        <tr><td></td><td></td><td></td><td></td></tr>
        <tr><td></td><td></td><td></td><td></td></tr>
        <tr><td></td><td></td><td></td><td></td></tr>
      </tbody>
    </table>
  </section>

  <section class="panel jobs">
    <div class="panel-head"><svg viewBox="0 0 20 20"><rect x="3" y="3" width="14" height="15" rx="1"/><path d="M7 2h6v3H7zM6.5 11l2.5 2.5 4.5-5"/></svg>Active Jobs</div>
    <table>
      <colgroup><col style="width:86px"><col style="width:95px"><col style="width:75px"><col style="width:101px"><col></colgroup>
      <thead><tr><th>Job#</th><th>Job Name</th><th>Status</th><th>Credit Limit</th><th>Avail. Credit</th></tr></thead>
      <tbody>
        <tr><td>pc101-001</td><td>Job-001</td><td>Active</td><td class="num">$50,100.00</td><td class="num">$35,100.00</td></tr>
        <tr><td>pc101-002</td><td>Job-002</td><td>Active</td><td class="num">$40,000.00</td><td class="num">$2000.00</td></tr>
        <tr><td>pc101-003</td><td>Job-003</td><td>Active</td><td class="num">$22,000.00</td><td class="num">$0.00</td></tr>
        <tr><td>pc101-004</td><td>Job-004</td><td>Active</td><td class="num">$10,400.00</td><td class="num">$10,400.00</td></tr>
        <tr><td></td><td></td><td></td><td></td><td></td></tr>
      </tbody>
    </table>
  </section>
</div>
</body>
</html>
```